The Brindle Tap Pub Needs A Bottle Label Design

Our gin supplier has created a fantastic bespoke Gin for our micro pub.
The new gin has serval blended ingredients and will be on sale from the 1st July 2017.
The bottle will be a clear 700ml glass style, similar to the attached picture. We would like the design to look as though it has been hand drawn on to the bottle, (line art style) and the background should be transparent.
Once we have confirmed the alcohol volume, this will be need to be included. We believe it to be aprox 40% abv.
Our pub is situated in the Old Swan area of Liverpool, UK and we would be happy for a Swan silhouette and line drawn ingredients to be part of the design.

The label design should have the following text:
The Brindle Tap Gin #1

```html
<!DOCTYPE html>
<html lang="en">
<head>
<meta charset="utf-8">
<title>The Brindle Tap Gin #1 – Bottle Label</title>
<link href="https://fonts.googleapis.com/css2?family=Old+Standard+TT:wght@700&family=Great+Vibes&family=Open+Sans:wght@400;500&display=swap" rel="stylesheet">
<style>
  :root {
    --bg: #ffffff;
    --navy: #27336f;
    --ink: #1a1a1a;
    --scene-dark: #3a3a3a;
    --scene-mid: #9a9a9a;
    --scene-light: #f2f2f2;
  }
  * { margin: 0; padding: 0; box-sizing: border-box; }
  html, body {
    width: 1200px;
    height: 1200px;
    overflow: hidden;
    background: var(--bg);
  }
  .label {
    position: relative;
    width: 1200px;
    height: 1200px;
    color: var(--ink);
  }
  .label__eyebrow {
    position: absolute;
    top: 78px;
    left: 0;
    width: 100%;
    text-align: center;
    font-family: "Open Sans", sans-serif;
    font-size: 30px;
    letter-spacing: 0.5px;
  }
  .label__title {
    position: absolute;
    top: 128px;
    left: 0;
    width: 100%;
    text-align: center;
    font-family: "Old Standard TT", serif;
    font-weight: 700;
    font-size: 104px;
    line-height: 1;
    color: var(--navy);
    transform: scaleX(0.72);
    white-space: nowrap;
  }
  .label__number {
    position: absolute;
    top: 240px;
    left: 820px;
    font-family: "Old Standard TT", serif;
    font-weight: 700;
    font-size: 104px;
    line-height: 1;
    color: var(--navy);
    transform: scaleX(0.8);
    transform-origin: left center;
  }
  .label__scene {
    position: absolute;
    top: 360px;
    left: 150px;
    width: 900px;
    height: 540px;
  }
  .label__grade {
    position: absolute;
    top: 925px;
    left: 0;
    width: 100%;
    text-align: center;
    font-family: "Great Vibes", cursive;
    font-size: 88px;
    line-height: 1;
  }
  .label__process {
    position: absolute;
    top: 1045px;
    left: 0;
    width: 100%;
    text-align: center;
    font-family: "Open Sans", sans-serif;
    font-weight: 500;
    font-size: 40px;
    letter-spacing: 2px;
  }
  .label__volume {
    position: absolute;
    top: 1115px;
    left: 0;
    width: 100%;
    text-align: center;
    font-family: "Open Sans", sans-serif;
    font-size: 28px;
  }
</style>
</head>
<body>
  <main class="label">
    <p class="label__eyebrow">KESTREL LANE DRY GIN</p>
    <h1 class="label__title">THE BRINDLE TAP GIN</h1>
    <p class="label__number">#1</p>

    <svg class="label__scene" viewBox="0 0 900 540" role="img" aria-label="Line-art illustration of a swan with raised wings on a pond, framed by juniper and botanical plants on the left and a pub house with shrubs on the right">
      <defs>
        <linearGradient id="sceneTone" x1="0" y1="0" x2="0" y2="1">
          <stop offset="0" stop-color="var(--scene-light)"/>
          <stop offset="0.65" stop-color="var(--scene-mid)"/>
          <stop offset="1" stop-color="var(--scene-dark)"/>
        </linearGradient>
      </defs>
      <rect x="0" y="0" width="900" height="540" rx="6" fill="url(#sceneTone)"/>
    </svg>

    <p class="label__grade">Premuim</p>
    <p class="label__process">TRIDESTILLED</p>
    <p class="label__volume">70CL. 42%VOL</p>
  </main>
</body>
</html>
```